Stationery Design Project - Professional Training Company

Full set of statinery in PDF and format that can be given to the printers

Letterhead
Business cards x 3
Compliments slip
Envelope
Updates

Many thanks for all your contributions, the quality of the designs is amazing.

Thank you all so much for your contribution to this project, I am very impressed with the designs and choice of designs, you are all clearly very talented individuals.

I hope to be making a decision on the final choice this evening UAE time.

Best regards and again thank you so much

Gordon

I would like to take this opportunity to thank you all for your contributions, I have been very impressed with each of the designs submitted.

I will shortly go back and give each of you a personal rating on each of your designs.

Again thank you all so much for your efforts

Best Regards

Gordon

Target Market(s)

We are a training company that provides IT training for Medical and Professional Staff, we train professional adults

Industry/Entity Type

Business

Requirements
Must have
• The letterhead and compliments slip must have at the bottom of the page:-

Bright Ledger Pathways LLP operates as a limited liability partnership registered in England and Wales (with registered number OC702614)

Business Cards are to be made up for three people (details of those to be provided after appoval of design but are included in this project) and should contain:

Name
Title
Telephone
email
Address: P.O. Box 418263 Dubai UAE
web address: www.brightledgerpathways.example
Nice to have
• Very clean and professional looking
Should not have
• No look to busy or ovr crowded

```html
<!DOCTYPE html>
<html lang="en">
<head>
<meta charset="utf-8">
<title>Bright Ledger Pathways LLP – Compliments Slip</title>
<link href="https://fonts.googleapis.com/css2?family=Ubuntu:wght@400;500&display=swap" rel="stylesheet">
<style>
  :root {
    --backdrop: #e6e4e0;
    --paper: #ffffff;
    --ink: #1e1e1e;
    --plum: #7b1b61;
    --leaf: #3f8f2a;
    --rule: #8e3b7a;
  }
  * { box-sizing: border-box; margin: 0; padding: 0; }
  html, body {
    width: 1200px;
    height: 720px;
    overflow: hidden;
    background: var(--backdrop);
    font-family: "Ubuntu", sans-serif;
  }
  .compliments-slip {
    position: absolute;
    left: 80px;
    top: 115px;
    width: 1040px;
    height: 490px;
    background: var(--paper);
    box-shadow: 0 6px 24px rgba(0,0,0,0.18);
    color: var(--ink);
  }
  .brand {
    position: absolute;
    left: 44px;
    top: 42px;
    display: flex;
    align-items: center;
    gap: 12px;
  }
  .brand-dot {
    width: 34px;
    height: 34px;
    border-radius: 50%;
    background: var(--leaf);
  }
  .brand-name {
    font-size: 26px;
    font-weight: 500;
    color: var(--ink);
    letter-spacing: -0.2px;
  }
  .salutation {
    position: absolute;
    right: 44px;
    top: 118px;
    font-size: 30px;
    font-weight: 400;
    color: var(--plum);
  }
  .contact-block {
    position: absolute;
    left: 44px;
    top: 318px;
    width: 420px;
    border-top: 1.5px solid var(--rule);
    padding-top: 12px;
    font-size: 15px;
    line-height: 1.45;
  }
  .contact-web { color: var(--plum); }
  .legal-note {
    position: absolute;
    left: 44px;
    right: 44px;
    bottom: 34px;
    font-size: 16px;
    color: var(--ink);
  }
</style>
</head>
<body>
  <main class="compliments-slip">
    <header class="brand">
      <span class="brand-dot" aria-hidden="true"></span>
      <span class="brand-name">Bright Ledger Pathways</span>
    </header>

    <p class="salutation">With compliments</p>

    <address class="contact-block" style="font-style: normal;">
      <div class="contact-line">(221) 33 410 27 58 | name@brightledgerpathways.example</div>
      <div class="contact-line">P.O. Box 418263 Dubai UAE</div>
      <div class="contact-web">www.brightledgerpathways.example</div>
    </address>

    <p class="legal-note">Bright Ledger Pathways LLP operates as a limited liability partnership registered in England and Wales (with registered number OC702614)</p>
  </main>
</body>
</html>
```